Bref créative
Complete Stationery Project for KMT
KMT - Real Estate Agency and Education Centre
I need double sided standard sized Business Card [3.5" x 2"]
Fonts and tag lines remain same font. Other texts, we're open to ideas from designers
Simple
Hendra Wiratmo
Owner / Realtor
Wisma Cakra Baruna 11 Floor
Jl. Raya Pemuda Kav. 3-4
Pasir Melati - Kebon Sirih
Jakarta Pusat - 10390
hendrawira@mailbox-example.com
www.hendra-wiratmo-example.com
K98765432
We require 2 different designs for 2 different companies. One is a real estate agency, the other is an education centre which provides courses in real estate, sales, motivation and personal development.
For the real estate agency:
- Name of company is P.T. Kirana Maju Teguh
- logo used shall be without the tagline
- tagline "The Heart of Property" to be placed separately
- we would like to see designs with and without personal photo, as not all agents might be placing their photos.
- Photos should not be in a box
- Name and Cell number needs to be more prominent than other details
- Design should be clean and exudes a branding of professionalism, trustworthiness and respect
For the education centre:
- Name of company is P.T. Sinar Budaya Akademi
- designs will be without photo
- name and cell number need NOT be more prominent
- design should be clean and corporate that exudes a branding of professionalism, reliability and trust
We require designs for:
- Business cards
- Open Top DL Envelopes 110mm x 220mm (plain)
- Open End DL Envelopes 110mm x 220mm (with window)
- Letter head
- Fax Cover
- 2 pocket folder with business card slot
- Open end envelopes 9 ½” x 12 ½”
Colours schemes are important to us to avoid 'clashes' with 'fengshui".
Colours allowed:
- Grey
Colours to be avoided:
- Yellow(and all other earthy colours)
- Green
- Brown(and all other woody colours)
- Red
We are open to ideas, but it should include the logo with tagline
Business card for the agency should also have the words "Buy / Sell / Lease"

```html
<!DOCTYPE html>
<html lang="en">
<head>
<meta charset="utf-8">
<title>KMT Business Cards</title>
<link href="https://fonts.googleapis.com/css2?family=Arimo:ital,wght@0,400;0,700;1,400&display=swap" rel="stylesheet">
<style>
  :root {
    --backdrop: #e6e8eb;
    --card-white: #ffffff;
    --card-shade: #eef0f3;
    --brand-blue: #1d6fb8;
    --brand-navy: #0f3f7a;
    --deep-blue: #0c4f95;
    --light-blue: #3f9ad8;
    --ink: #1f2a36;
    --muted: #56606b;
  }
  * { margin: 0; padding: 0; box-sizing: border-box; }
  html, body { width: 1200px; height: 842px; overflow: hidden; }
  body {
    background: var(--backdrop);
    font-family: "Arimo", Arial, sans-serif;
    color: var(--ink);
    position: relative;
  }
  .card {
    position: absolute;
    width: 500px;
    height: 286px;
    border-radius: 16px;
    box-shadow: 0 6px 18px rgba(20, 35, 55, 0.18);
    overflow: hidden;
  }
  .card--front { left: 70px; top: 170px; background: linear-gradient(180deg, var(--card-white), var(--card-shade)); }
  .card--back-blue { left: 630px; top: 120px; background: radial-gradient(ellipse at 30% 35%, var(--light-blue) 0%, var(--brand-blue) 45%, var(--deep-blue) 100%); }
  .card--back-white { left: 360px; top: 500px; background: linear-gradient(180deg, var(--card-white), var(--card-shade)); }

  .watermark {
    position: absolute; left: 20px; top: 0; width: 200px; height: 286px;
    border-radius: 50% 50% 0 0;
  }
  .card--back-blue .watermark { background: radial-gradient(ellipse at 50% 40%, rgba(255,255,255,0.16), rgba(255,255,255,0) 70%); }
  .card--back-white .watermark { background: radial-gradient(ellipse at 50% 40%, rgba(29,111,184,0.10), rgba(29,111,184,0) 70%); }

  .brand { display: flex; align-items: center; gap: 10px; }
  .brand__dot { width: 14px; height: 14px; border-radius: 50%; background: var(--brand-blue); }
  .brand__name { font-weight: 700; color: var(--brand-navy); letter-spacing: 1px; line-height: 1; }
  .brand--front { position: absolute; left: 28px; top: 40px; }
  .brand--front .brand__name { font-size: 46px; }
  .company-name { position: absolute; left: 52px; top: 92px; font-size: 11px; color: var(--brand-navy); }
  .tagline { font-style: italic; font-size: 10px; color: var(--brand-navy); }
  .tagline--front { position: absolute; left: 110px; top: 108px; font-size: 8px; }

  .details { position: absolute; left: 28px; top: 150px; font-size: 10px; line-height: 13px; color: var(--ink); list-style: none; }

  .portrait {
    position: absolute; left: 306px; top: 26px; width: 150px; height: 164px;
    background: linear-gradient(180deg, #7c8896 0%, #4a5563 55%, rgba(238,240,243,0) 100%);
    -webkit-mask-image: radial-gradient(ellipse at 50% 45%, #000 55%, transparent 75%);
    mask-image: radial-gradient(ellipse at 50% 45%, #000 55%, transparent 75%);
  }
  .agent { position: absolute; left: 290px; top: 196px; width: 182px; text-align: center; }
  .agent__name { font-size: 17px; font-weight: 700; color: var(--brand-navy); }
  .agent__role { font-size: 10px; color: var(--muted); margin-top: 3px; }
  .agent__cell { font-size: 12px; font-weight: 700; color: var(--brand-navy); margin-top: 3px; }
  .services { font-size: 9px; letter-spacing: 1px; color: var(--brand-blue); margin-top: 6px; }

  .back-lockup { position: absolute; right: 50px; top: 118px; text-align: left; }
  .back-lockup .brand__name { font-size: 40px; }
  .back-lockup .tagline { margin: 4px 0 0 90px; }
  .card--back-blue .brand__name, .card--back-blue .tagline { color: var(--card-white); }
  .card--back-blue .brand__dot { background: var(--card-white); }
  .back-rule { height: 1px; width: 200px; margin-top: 6px; background: var(--brand-navy); opacity: 0.4; }
  .card--back-blue .back-rule { background: var(--card-white); }
</style>
</head>
<body>

<section class="card card--front">
  <div class="brand brand--front">
    <span class="brand__dot"></span>
    <span class="brand__name">KMT</span>
  </div>
  <p class="company-name">P.T. Kirana Maju Teguh</p>
  <p class="tagline tagline--front">The Heart of Property</p>
  <ul class="details">
    <li>Wisma Cakra Baruna 11 Floor</li>
    <li>Jl. Raya Pemuda Kav. 3-4</li>
    <li>Pasir Melati - Kebon Sirih</li>
    <li>Jakarta Pusat - 10390</li>
    <li>Phone: +62 2150 3377</li>
    <li>Fax: +62 2150 3378</li>
    <li>Email: hendrawira@mailbox-example.com</li>
    <li>Web: www.hendra-wiratmo-example.com</li>
  </ul>
  <div class="portrait" role="img" aria-label="Portrait photo of the agent"></div>
  <div class="agent">
    <p class="agent__name">Hendra Wiratmo</p>
    <p class="agent__role">Owner / Realtor</p>
    <p class="agent__cell">Cell: +62 812 4470 2196</p>
    <p class="services">Buy / Sell / Lease</p>
  </div>
</section>

<section class="card card--back-blue">
  <div class="watermark" role="img" aria-label="Faint decorative emblem"></div>
  <div class="back-lockup">
    <div class="brand">
      <span class="brand__dot"></span>
      <span class="brand__name">KMT</span>
    </div>
    <div class="back-rule"></div>
    <p class="tagline">The Heart of Property</p>
  </div>
</section>

<section class="card card--back-white">
  <div class="watermark" role="img" aria-label="Faint decorative emblem"></div>
  <div class="back-lockup">
    <div class="brand">
      <span class="brand__dot"></span>
      <span class="brand__name">KMT</span>
    </div>
    <div class="back-rule"></div>
    <p class="tagline">The Heart of Property</p>
  </div>
</section>

</body>
</html>
```